Web Design for US Hispanic Business Community

Zep Tal Group aka www.MarlowVentura.TV is a dynamic new entrant in the the Hispanic internet small business solutions and services marketplace, through - engaging easy to use start-up business solutions.

Marlow Ventura TV will feature a local online production of a weekly lifestyle show surrounded around community interest. Video news, business, Fashion and food channels and other topics around the Hispanic lifestyle trends in local Colorado area and across the US.

MVTV also provides budding Hispanic entrepreneurs a one stop shopping spot, providing access, participation and guidance including coaching, that may have been unattainable in the past, due to U.S job market shortages. For those Hispanics who want to to move into the business world and attain an improved and better quality of life.

To established sme's including e-commerce businesses and traditional retailers, MVTV will provide a platform from which to leverage Hispanic market share and brand positioning. Content on this site will also attract and engage Businesses, CEO's and budding entrepreneurs.

Solutions offered on Marlow Ventura TV

Focused and tightly targeted Audience
Strategic Marketing Solutions (sem/seo/social media)
Education and Learning
Custom Content Creation
Product Placement
How to videos
Daily Deals
CEO Corner

Objective of this web portal: Marlow Ventura TV will build a unique internet portal site, like no other and combind this with unique products and services that will guide both businesses and consumers to the site. This internet portal will be the the first point of contact for all those engaging in Marlow Ventura TV and will be the point from which users start to interact with the portal. Ideally, this will be the first point from which Hispanics in the US start all internet activity.

Design Needs (Please note this is design only, Coding/development to be done by someone else):

I will be using a Wordpress CMS so please keep this in mind.

I'll be needing design for the following 4 main pages and the 5 "templates" below. I have attached the Logo to work with. Please note the font used in the circles can be customised if you think there is a better choice.

Web Portal must have
1) Customised Home Page (creative & Original layouts PLEASE!!!
2) Customised Marketplace page (This page highlights all the products and services on offer through the site)
3) Customised Entertainment and Dining Page (with a fashionable and funky icon. This page will drive high traffic)
4)A Community Upload Page - This will be user generated content, you could potentially use the circles of the logo to mark video content (there is also potential to use one or more of the coloured circles with a little video camera beside it)

Template layouts for 5 other following pages.

5 other pages include -

News Channel, Health and Lifestyle, Fashion, Food and Recipes and Daily Deals (This could be a plugin but I'd probably still want it customised).

I have included here example of web layout I like, esp for home page(Brisk Parlor TV) http://briskparlor.tv/video-library/brisk-parlor-june-25-2012

I have attached a design map of home page design I like.

I have attached a flow chart on the content that will be uploaded on each page (Take note where RSS feeds fit in)

I have included in 'Nice to have' a link of a 'slide' that I would also like on the home page http://quillmarket.net/item/community/512847?WT.ac=category_thumb&WT.seg_1=category_thumb&WT.z_author=pebblor

Please see all attached documents and links included.
Updates

I need to see original layout concepts, Please!!!

Please make header logo Dominant...I also added an image that I think would look cool for the blogging images...

Added a couple new logo files please replace with this one. lso I created a logo for my UGC Video upload, that needs to be featured in middle of page and on the footer

Target Market(s)

25- 49 year old U.S Hispanics and those in business. Hispanic communities usage rates of Smartphones, Television, Online Video and Social networking and other forms of entertainment make this group one of todays most engaged populations in todays digital space. Following Trends of this group mean that according to Varrick reasecrh this group send 941 txt msgs a month, more then any other ethnic group and are 25% more likely to follow a brand and 18% more likely to follow a celebrity then any other online group.

Industry/Entity Type

E-Commerce

Requirements
Must have
• Must have a corporate, Tech savvy design feel (not over the top). This is a professional, but hip and fashionable site.
White Background
The ability to fit RSS video Feeds
Entertainment and Dining page must have radio box or a cool icon to customize it as fashionable entertainment page, as this page will land majority traffic.
SEE FLOW CHART ON WEB LAYOUT ATTACHED
Nice to have
• Experiment with the text color in slogan line, & font style in circles of logo.
Homepage including Slider (I have below is a link to a website that I am happy with the look of the slider on)
http://quillmarket.net/item/community/512847?WT.ac=category_thumb&WT.seg_1=category_thumb&WT.z_author=pebblor
Should not have
• Must not be cartoony or childish

6/27 Update,
I uploaded a image of slider I like at lumorava.com (video tab,check it out)I love the functionality of it-this is hm pg screen we need wow factor!, I need banners on each side if possible or a creative way to find some banner ad space. I also uploaded MVTV Logo B Colors file try using the 1st image at top of page, need to see examples with this logo as well!

```html
<!DOCTYPE html>
<html lang="en">
<head>
<meta charset="utf-8">
<title>MarlowVentura.TV</title>
<link href="https://fonts.googleapis.com/css2?family=Ubuntu:wght@400;500;700&family=Open+Sans:wght@400;600;700&display=swap" rel="stylesheet">
<style>
:root{
  --page:#e9e9e9;
  --paper:#ffffff;
  --ink:#3a3a3a;
  --muted:#6b6b6b;
  --blue:#1c57a5;
  --link:#1f5fb0;
  --nav-top:#3f7ed0;
  --nav-bot:#12478f;
  --footer-ink:#e4e4e4;
}
*{box-sizing:border-box;margin:0;padding:0}
html,body{width:686px;height:1200px;overflow:hidden}
body{background:var(--page);font-family:"Open Sans",sans-serif;color:var(--ink);position:relative}
.abs{position:absolute}
.sheet{left:58px;top:0;width:570px;height:1090px;background:var(--paper)}
/* brand */
.brand{display:flex;align-items:center;gap:6px;font-family:"Ubuntu",sans-serif;font-weight:500;color:#2d2d2d;white-space:nowrap}
.brand .dot{width:15px;height:15px;border-radius:50%;background:#e0682b;flex:none}
.head-brand{left:64px;top:30px;font-size:17px}
/* header */
.topad{left:230px;top:21px;width:267px;height:34px;background:linear-gradient(90deg,#1d3f8e,#2a64c2 60%,#1a3d86);border:1px solid #10295e;color:#fff;padding:3px 0 0 70px;overflow:hidden}
.topad .t{font-family:"Ubuntu",sans-serif;font-size:12px;line-height:14px}
.topad .s{font-size:5.5px;line-height:7px}
.topad .new{position:absolute;right:4px;top:2px;font-family:"Ubuntu",sans-serif;font-weight:700;font-size:9px;color:#fff;background:#f29a1c;padding:1px 5px}
.topad .mark{position:absolute;left:8px;top:4px;width:24px;height:24px;background:#fff;opacity:.85}
.search{left:520px;top:8px;width:96px}
.search .name{font-family:"Ubuntu",sans-serif;font-size:14px;color:#2f5fb3;text-align:center}
.search .box{height:12px;border:1px solid #d8d8d8;background:#f7f7f7;font-size:5.5px;color:#aaa;padding:2px 4px;margin-top:2px}
/* nav */
.nav{left:50px;top:74px;width:586px;height:24px;background:linear-gradient(var(--nav-top),var(--nav-bot));display:flex;align-items:center}
.nav a{flex:auto;text-align:center;color:#fff;font-size:7.5px;text-decoration:none;line-height:24px;border-right:1px solid rgba(255,255,255,.2)}
.nav a.on{background:#2c2c2c;flex:0 0 72px}
/* slider */
.slider{left:64px;top:106px;width:558px;height:122px;background:linear-gradient(#f2f2f2,#dedede);border:1px solid #d0d0d0;border-radius:6px}
.arrow{width:18px;height:28px;background:#fff;border:1px solid #bbb;border-radius:14px;top:154px;display:flex;align-items:center;justify-content:center}
.thumb{top:118px;width:112px;height:100px;border:2px solid #fff;box-shadow:0 1px 3px rgba(0,0,0,.3)}
.play{position:absolute;width:18px;height:18px;border-radius:50%;background:rgba(0,0,0,.7);border:1.5px solid #fff;left:50%;top:50%;transform:translate(-50%,-50%)}
.play::after{content:"";position:absolute;left:6px;top:4px;border-left:6px solid #fff;border-top:4px solid transparent;border-bottom:4px solid transparent}
/* feature */
.feature{left:68px;top:251px;width:309px;height:157px;border:2px solid var(--blue);border-radius:4px;background:linear-gradient(#2d6fc4,#0e3f84);overflow:hidden}
.feature .txt{position:absolute;left:5px;top:18px;width:118px;color:#fff}
.feature h2{font-family:"Ubuntu",sans-serif;font-weight:400;font-size:11.5px;line-height:17px}
.feature h2 b{font-weight:700}
.feature p{font-size:5.6px;line-height:10px;margin-top:8px;text-align:justify}
.feature .img{position:absolute;left:126px;top:0;width:181px;height:153px;background:linear-gradient(135deg,#f4f4f4,#cfd2d6)}
.dots{position:absolute;left:9px;bottom:11px;display:flex;gap:5px}
.dots i{width:6px;height:6px;border-radius:50%;background:#fff}
.fbrand{position:absolute;left:132px;top:8px;font-family:"Ubuntu",sans-serif;font-weight:500;font-size:7px;color:#333}
.h{font-family:"Ubuntu",sans-serif;font-weight:500;color:#444}
.adv{left:392px;top:250px;font-size:11px}
.advvid{left:392px;top:267px;width:214px;height:139px;background:#111;border:1px solid #333}
.advvid .pic{height:118px;background:linear-gradient(120deg,#4b1d5e,#c23b8c 40%,#3a8fc2 70%,#1a1a2a)}
.bar{height:12px;background:#2a2a2a;border-top:1px solid #444}
/* blog cards */
.card{top:436px;width:107px;height:114px;background:linear-gradient(#fff,#f1f1f1);border:1px solid #e6e6e6;border-radius:5px;padding:6px 5px}
.card h3{font-family:"Ubuntu",sans-serif;font-weight:500;font-size:10px;color:#444;display:flex;align-items:center;gap:4px}
.card h3 i{width:12px;height:12px;border-radius:50%;background:var(--blue)}
.entry{display:flex;gap:5px;margin-top:8px;font-size:6.3px;line-height:9px;color:#666}
.entry .ph{width:35px;height:23px;background:linear-gradient(#eee,#bdbdbd);position:relative;flex:none}
.entry b{color:var(--link);font-weight:600}
/* tabs */
.tabs{left:422px;top:422px;display:flex;gap:3px}
.tabs span{font-size:6.5px;padding:3px 9px;border-radius:6px 6px 0 0;background:#555;color:#fff}
.tabs span.on{background:var(--blue)}
.popular{left:414px;top:436px;width:196px;height:244px;background:#fafafa;border:1px solid #e6e6e6;border-radius:5px;padding:10px 0 0 14px}
.pitem{display:flex;gap:6px;margin-bottom:11px;font-size:6px;line-height:9.2px;color:#666}
.pitem .ph{width:69px;height:43px;flex:none;position:relative;background:linear-gradient(#d9d9d9,#6d6d6d)}
.pitem b{color:var(--link);font-weight:600;display:block}
.more{position:absolute;right:10px;bottom:10px;font-size:6.5px;color:var(--link);font-style:italic;text-decoration:underline}
/* players */
.player{width:139px;height:96px;background:#111;border:1px solid #555;padding:4px 2px 0}
.player .cap{font-size:4px;color:#eee;height:6px;white-space:nowrap;overflow:hidden}
.player .pic{height:74px;position:relative}
.player .ctl{height:10px;background:#1a1a1a;border-top:1px solid #3a3a3a}
/* market / deal */
.market{left:63px;top:690px;width:158px;height:90px;background:linear-gradient(#fff,#f0f0f0);border:1px solid #e4e4e4;border-radius:5px}
.market h3{position:absolute;left:44px;top:9px;font-size:10px}
.market p{position:absolute;left:9px;top:29px;width:48px;font-size:6.3px;line-height:9px;color:#666}
.market .pic{position:absolute;left:60px;top:26px;width:90px;height:60px;background:linear-gradient(#f3f3f3,#d7d2cb)}
.deal{left:234px;top:690px;width:159px;height:89px;border-radius:5px;background:linear-gradient(90deg,#d8d8d8 45%,#7cc12a 45%);overflow:hidden}
.deal .pic{position:absolute;left:8px;top:10px;width:62px;height:70px;background:linear-gradient(135deg,#f6a21d,#2a9be0)}
.deal .t1{position:absolute;left:86px;top:14px;font-family:"Ubuntu",sans-serif;font-weight:700;font-size:13px;color:#fff}
.deal .t2{position:absolute;left:86px;top:34px;font-family:"Ubuntu",sans-serif;font-weight:700;font-size:10.5px;color:#fff}
.deal .t3{position:absolute;left:86px;top:49px;width:64px;font-size:3.8px;color:#eaf7d7}
/* newsletter */
.news{left:414px;top:710px;width:196px;height:146px;background:#f7f7f7;border:1px solid #e6e6e6;border-radius:5px}
.news h3{position:absolute;left:38px;top:11px;font-size:10px}
.news h3 b{color:var(--blue);font-weight:500}
.news .env{position:absolute;left:10px;top:7px;width:22px;height:17px;background:#f3c12b;border:1px solid #d59a10}
.news p{position:absolute;left:8px;top:32px;width:180px;font-size:5.8px;line-height:10px;color:#666;text-align:justify}
.field{position:absolute;left:6px;font-size:6.5px;color:#555;display:flex;align-items:center;gap:6px}
.field span{width:72px;text-align:right;white-space:nowrap}
.field i{width:104px;height:12px;border:1px solid #ddd;border-radius:6px;background:#fff}
.btn{background:linear-gradient(#3a7fd6,#0f4592);color:#fff;font-size:6.8px;border-radius:9px;border:1px solid #0a3572;text-align:center}
/* rss */
.ent{left:68px;top:796px;width:333px;height:78px;background:linear-gradient(#fff,#f2f2f2);border:1px solid #e4e4e4;border-radius:5px}
.ent h3{position:absolute;left:26px;top:8px;font-size:10px}
.note{position:absolute;left:8px;top:5px;width:14px;height:18px;background:#7fb22b;border-radius:50% 50% 50% 0}
.rss{position:absolute;top:30px;display:flex;gap:7px;font-size:6px;line-height:9.3px;color:#666}
.rss .ph{width:54px;height:36px;flex:none;background:linear-gradient(#e9e9e9,#8e8e8e);position:relative}
.rss b{font-weight:600;color:#444;display:block}
.sect{font-size:11px}
.episodes{left:418px;top:882px;width:196px;height:124px;border:2px solid #111;background:#fff}
.episodes h3{position:absolute;left:12px;top:7px;font-size:9.5px}
.episodes .ep-brand{position:absolute;left:0;right:0;top:70px;justify-content:center;font-size:14px}
.episodes .ctl{position:absolute;left:-2px;right:-2px;bottom:-2px;height:13px;background:#e5e5e5;border-top:1px solid #bbb;font-size:5.5px;color:#333;padding:3px 0 0 90px}
/* insurance */
.ins{left:136px;top:1029px;width:416px;height:51px;border:1px solid #ccc;background:linear-gradient(90deg,#fff 18%,#5bb12a 18%,#2e8a1c 62%,#f3e9d8 78%)}
.ins .nm{position:absolute;left:10px;top:15px;font-family:"Ubuntu",sans-serif;font-weight:500;font-size:9px;color:#3a7f1c}
.ins .big{position:absolute;left:122px;top:2px;font-family:"Ubuntu",sans-serif;font-weight:700;font-size:12px;color:#fff;line-height:13px;text-align:center}
.ins .big em{color:#f7e34b}
.ins .small{position:absolute;left:92px;top:33px;font-size:6px;color:#fff;font-weight:600;line-height:8px}
.ins .small b{color:#f7e34b}
.ins .cta{position:absolute;left:268px;top:26px;width:76px;height:19px;border-radius:10px;background:linear-gradient(#e0302a,#9c0f0c);color:#fff;font-size:8px;font-style:italic;text-align:center;line-height:19px}
.ins .pic{position:absolute;right:0;top:0;width:70px;height:49px;background:linear-gradient(#f6e3cd,#e0b98e)}
/* footer */
.footer{left:50px;top:1086px;width:586px;height:114px;background:linear-gradient(#2f2f2f,#4a4a4a)}
.foot-brand{position:absolute;left:18px;top:48px;font-size:14px;color:var(--footer-ink)}
.foot-brand .dot{background:#cfcfcf}
.fcol{position:absolute;top:19px;color:var(--footer-ink)}
.fcol h4{font-family:"Ubuntu",sans-serif;font-weight:500;font-size:10px;margin-bottom:8px}
.fcol li{list-style:none;font-size:6.2px;margin-bottom:6.5px;display:flex;align-items:center;gap:5px}
.fcol .soc li{font-style:italic;text-decoration:underline}
.fcol .soc li i{width:8px;height:8px;background:#4d84c6;flex:none}
.fcol .all li::before{content:"";border-left:3px solid #fff;border-top:2.5px solid transparent;border-bottom:2.5px solid transparent}
.mv3{display:flex;gap:10px}
.mv3 div{width:44px;height:29px;border:1px solid #999;background:linear-gradient(#e6a93a,#8a5a21);position:relative}
.mv3 .play{width:12px;height:12px}
.mv3 .play::after{left:3.5px;top:2px;border-left-width:4px;border-top-width:3px;border-bottom-width:3px}
</style>
</head>
<body>
<div class="abs sheet"></div>

<header>
  <div class="abs brand head-brand"><span class="dot"></span>MarlowVentura.TV</div>
  <div class="abs topad">
    <span class="mark"></span>
    <div class="t">GlyphForge 6</div>
    <div class="s">The Professional Icon Authoring Tool</div>
    <div class="s">Build crisp icons for any desktop</div>
    <span class="new">NEW!</span>
  </div>
  <div class="abs search">
    <div class="name">Seekwell</div>
    <div class="box">Seekwell Search</div>
  </div>
</header>

<nav class="abs nav">
  <a class="on">News Channels</a><a>health &amp; Salud!</a><a>fashion / lifestyle</a><a>marketplace</a><a>Entertainment / Dinning</a><a>Food Recipies</a><a>Deals</a>
</nav>

<section>
  <div class="abs slider"></div>
  <div class="abs arrow" style="left:73px"><svg width="8" height="10"><path d="M7 0 1 5l6 5" fill="none" stroke="#333" stroke-width="2"/></svg></div>
  <div class="abs arrow" style="left:596px"><svg width="8" height="10"><path d="M1 0l6 5-6 5" fill="none" stroke="#333" stroke-width="2"/></svg></div>
  <div class="abs thumb" style="left:98px;background:linear-gradient(90deg,#c0542e,#5a2b6f 55%,#7d3a8c)" role="img" aria-label="Video contest promotion with salon model"><span class="play"></span></div>
  <div class="abs thumb" style="left:226px;background:linear-gradient(#2fb3e2,#8fd6f0)" role="img" aria-label="Daily deal discount promotion"><span class="play"></span></div>
  <div class="abs thumb" style="left:351px;background:linear-gradient(90deg,#c0542e,#5a2b6f 55%,#7d3a8c)" role="img" aria-label="Video contest promotion with salon model"><span class="play"></span></div>
  <div class="abs thumb" style="left:476px;background:linear-gradient(#4c7a84,#24383d)" role="img" aria-label="Street fashion photo by the waterfront"><span class="play"></span></div>
</section>

<section>
  <div class="abs feature">
    <div class="txt">
      <h2>Solutions offered on<br><b>Marlow Ventura TV</b></h2>
      <p>Lorem Ipsum is simply dummy text of the printing and typesetting industry. Lorem Ipsum has been the industry's standard dummy text ever since the 1500s, when an unknown.</p>
    </div>
    <div class="img" role="img" aria-label="Cassette tape figure walking beside a laptop"><span class="play" style="width:30px;height:30px"></span></div>
    <div class="fbrand">MarlowVentura.TV</div>
    <div class="dots"><i></i><i></i><i></i><i></i><i></i><i></i><i></i></div>
  </div>
  <div class="abs h adv">Post your Ads here</div>
  <div class="abs advvid">
    <div class="pic" role="img" aria-label="Colorful music video still" style="position:relative"><span class="play"></span></div>
    <div class="bar"></div>
  </div>
</section>

<section>
  <div class="abs card" style="left:63px">
    <h3><i></i>Jo's Blog</h3>
    <div class="entry"><div class="ph"><span class="play" style="width:12px;height:12px"></span></div><div>Solving Equations<br>with a Variable<br><b>31,536 views</b></div></div>
    <div class="entry"><div class="ph"></div><div>Solving Equations<br>with a Variable<br><b>31,536 views</b></div></div>
  </div>
  <div class="abs card" style="left:178px">
    <h3><i></i>Latest Blog</h3>
    <div class="entry"><div class="ph"></div><div>Solving Equations<br>with a Variable<br><b>31,536 views</b></div></div>
    <div class="entry"><div class="ph"></div><div>Solving Equations<br>with a Variable<br><b>31,536 views</b></div></div>
  </div>
  <div class="abs card" style="left:293px">
    <h3><i></i>Latest Blog</h3>
    <div class="entry"><div class="ph"></div><div>Solving Equations<br>with a Variable<br><b>31,536 views</b></div></div>
    <div class="entry"><div class="ph"></div><div>Solving Equations<br>with a Variable<br><b>31,536 views</b></div></div>
  </div>

  <div class="abs tabs"><span class="on">Popular</span><span>Recent</span><span>Comment</span><span>Tags</span></div>
  <div class="abs popular">
    <div class="pitem"><div class="ph" role="img" aria-label="Silhouettes of people in a green field"><span class="play"></span></div><div><b>News signs $5.2m in e</b>Lorem Ipsum is simply dummy text of the printing and typeset-ting industry</div></div>
    <div class="pitem"><div class="ph" role="img" aria-label="Woman seated in a dark corridor"><span class="play"></span></div><div><b>News signs $5.2m in e</b>Lorem Ipsum is simply dummy text of the printing and typeset-ting industry</div></div>
    <div class="pitem"><div class="ph" role="img" aria-label="Grey bird in flight"><span class="play"></span></div><div><b>News signs $5.2m in e</b>Lorem Ipsum is simply dummy text of the printing and typeset-ting industry</div></div>
    <div class="pitem"><div class="ph" role="img" aria-label="Team meeting around a table" style="background:linear-gradient(#f0f0f0,#a9a9a9)"><span class="play"></span></div><div><b>News signs $5.2m in e</b>Lorem Ipsum is simply dummy text of the printing and typeset-ting industry</div></div>
    <span class="more">Read more</span>
  </div>

  <div class="abs player" style="left:76px;top:570px">
    <div class="cap">Box Selection and Multi-Line Editing Demo</div>
    <div class="pic" role="img" aria-label="News anchor in studio" style="background:linear-gradient(90deg,#1b3f96,#0e2466)"><span class="play"></span></div>
    <div class="ctl"></div>
  </div>
  <div class="abs player" style="left:253px;top:570px">
    <div class="cap">Box Selection and Multi-Line Editing Demo</div>
    <div class="pic" role="img" aria-label="Runner leaping on the beach" style="background:linear-gradient(#8fbfe0,#d9e8ef 70%,#c9b58f)"><span class="play"></span></div>
    <div class="ctl"></div>
  </div>
</section>

<section>
  <div class="abs market">
    <svg class="abs" style="left:8px;top:7px" width="34" height="18"><path d="M2 16 12 8l6 5 14-11" fill="none" stroke="#c3272b" stroke-width="2"/><path d="M26 2h6v6" fill="none" stroke="#c3272b" stroke-width="2"/></svg>
    <h3 class="h">Market Place</h3>
    <p>Lorem Ipsum is simply dummy text of the printing</p>
    <div class="pic" role="img" aria-label="Woman working at a laptop with pencils"><span class="play"></span></div>
  </div>
  <div class="abs deal">
    <div class="pic" role="img" aria-label="Daily deal price tags"><span class="play"></span></div>
    <div class="t1">Special</div>
    <div class="t2">DAILY DEAL!</div>
    <div class="t3">Attract customers with one deal a day</div>
  </div>
  <div class="abs news">
    <span class="env"></span>
    <h3 class="h">Subscribe to <b>Our Newsletter</b></h3>
    <p>Lorem Ipsum is simply dummy text of the printing and type-setting industry. Lorem Ipsum has been the industry's standard dummy text ever since the 1500s</p>
    <div class="field" style="top:76px"><span>Enter your Email</span><i></i></div>
    <div class="field" style="top:100px"><span>Enter your Password</span><i></i></div>
    <div class="abs btn" style="left:132px;top:122px;width:58px;height:17px;line-height:15px">Subscribe ›</div>
  </div>

  <div class="abs ent">
    <span class="note"></span>
    <h3 class="h">Entertainment &amp; Dining Rss Feed</h3>
    <div class="rss" style="left:10px"><div class="ph" role="img" aria-label="Team discussion at a desk"><span class="play" style="width:13px;height:13px"></span></div><div style="width:108px"><b>News signs $5.2m in e</b>Lorem Ipsum is simply dummy text of the printing and typeset-ting industry</div></div>
    <div class="rss" style="left:188px;top:36px"><div class="ph" role="img" aria-label="Colleagues reviewing documents"><span class="play" style="width:13px;height:13px"></span></div><div style="width:78px"><b>News signs $5.2m in e</b>Lorem Ipsum is simply dummy text of the printing</div></div>
  </div>

  <svg class="abs" style="left:68px;top:885px" width="20" height="22"><rect x="2" y="2" width="16" height="18" fill="#444"/><path d="M2 8h16M2 14h16M8 2v18M14 2v18" stroke="#fff"/></svg>
  <div class="abs h sect" style="left:97px;top:891px">Fashion Rss Feed</div>
  <svg class="abs" style="left:253px;top:886px" width="22" height="18"><path d="M3 1v16M1 1v5h4V1M11 1c3 0 3 6 0 6v10M16 2h5v6h-5zM18.5 8v9" stroke="#2563b0" stroke-width="2" fill="none"/></svg>
  <div class="abs h sect" style="left:279px;top:891px">Food Rss Feed</div>
  <div class="abs player" style="left:86px;top:920px;width:114px;height:78px">
    <div class="cap">Box Selection and Multi-Line Editing Demo</div>
    <div class="pic" role="img" aria-label="Fashion models in sunglasses" style="height:58px;background:linear-gradient(90deg,#5b4a45,#c6b9ad)"><span class="play"></span></div>
    <div class="ctl"></div>
  </div>
  <div class="abs player" style="left:253px;top:920px;width:114px;height:78px">
    <div class="cap">Box Selection and Multi-Line Editing Demo</div>
    <div class="pic" role="img" aria-label="Plate of fried appetizers" style="height:58px;background:linear-gradient(#e6a93a,#8a5a21)"><span class="play"></span></div>
    <div class="ctl"></div>
  </div>

  <div class="abs episodes">
    <h3 class="h">MVTV Episodes</h3>
    <span class="play" style="top:50px;width:22px;height:22px"></span>
    <div class="brand ep-brand"><span class="dot"></span>MarlowVentura.TV</div>
    <div class="ctl">0:10 / 1:53</div>
  </div>
</section>

<aside class="abs ins">
  <div class="nm">TrueLifePlan</div>
  <div class="big">Term Life Insurance<br><em>in Minutes</em></div>
  <div class="small">• Instant Coverage - If Qualified<br><b>• NO MEDICAL EXAM - Just a few health questions</b></div>
  <div class="cta">Click Here</div>
  <div class="pic" role="img" aria-label="Mother and daughter smiling"></div>
</aside>

<footer class="abs footer">
  <div class="brand foot-brand"><span class="dot"></span>MarlowVentura.TV</div>
  <div class="fcol" style="left:166px">
    <h4>Connect with Us</h4>
    <ul class="soc"><li><i></i>Follow Us on Chatterly</li><li><i></i>Follow Us on Peepline</li><li><i></i>Follow Us on RSS</li><li><i></i>Follow US on Linkvale</li><li style="padding-left:13px">Sitemap</li></ul>
  </div>
  <div class="fcol" style="left:300px">
    <h4>Most Viewed</h4>
    <div class="mv3"><div role="img" aria-label="Food dish"><span class="play"></span></div><div role="img" aria-label="Food dish"><span class="play"></span></div><div role="img" aria-label="Food dish"><span class="play"></span></div></div>
  </div>
  <div class="abs btn" style="left:396px;top:88px;width:58px;height:14px;line-height:12px">Subscribe ›</div>
  <div class="fcol" style="left:491px">
    <h4>All</h4>
    <ul class="all"><li>About us</li><li>Archive</li><li>Newsletter</li><li>Advertise</li><li>Contact</li></ul>
  </div>
</footer>
</body>
</html>
```